R&K Security Services PTY. LTD.

Ive just had my logo made and I'm looking for some simple but strong designs for my business cards the company is a security company.

Please use dark colors.

Regards,

Dale Prentiss

Reason: Need more time for discussion with other directors

Industry/Entity Type

Security

Font styles to use
Sans Serif
Decorative

```html
<!DOCTYPE html>
<html lang="en">
<head>
<meta charset="utf-8">
<title>R&amp;K Prentiss Security Services – Business Card</title>
<link href="https://fonts.googleapis.com/css2?family=Libre+Baskerville:wght@400;700&display=swap" rel="stylesheet">
<style>
  :root {
    --backdrop: #c9c9c9;
    --card-dark: #2f2f31;
    --card-light: #f7f7f5;
    --ink-light: #f1f1f1;
    --ink-muted: #a9a9ab;
    --ink-dark: #4a4a4c;
    --ink-soft: #7a7a7c;
    --rule: #8c8c8e;
  }
  * { margin: 0; padding: 0; box-sizing: border-box; }
  html, body { width: 1200px; height: 1000px; overflow: hidden; }
  body {
    background: var(--backdrop);
    font-family: "Libre Baskerville", Georgia, serif;
    position: relative;
  }
  .card {
    position: absolute;
    left: 250px;
    width: 700px;
    height: 400px;
    box-shadow: 0 8px 24px rgba(0,0,0,.18);
  }
  .card--back { top: 60px; background: var(--card-dark); color: var(--ink-light); }
  .card--front { top: 540px; background: var(--card-light); color: var(--ink-dark); }

  /* Back side */
  .back-brand {
    position: absolute;
    left: 70px; top: 168px;
    width: 250px;
    text-align: center;
  }
  .back-brand__name { font-size: 24px; letter-spacing: .5px; color: var(--ink-light); }
  .back-brand__tag { font-size: 12px; color: var(--ink-muted); margin-top: 4px; letter-spacing: .3px; }
  .back-divider {
    position: absolute;
    left: 350px; top: 100px;
    width: 1px; height: 200px;
    background: var(--rule);
  }
  .contact-list {
    position: absolute;
    left: 380px; top: 112px;
    list-style: none;
  }
  .contact-list__item {
    display: flex; align-items: center;
    font-size: 14px; letter-spacing: .3px;
    height: 30px;
    color: var(--ink-light);
  }
  .contact-list__icon { width: 16px; height: 16px; margin-right: 12px; flex: none; }

  /* Front side */
  .front-mark {
    position: absolute;
    left: 50%; top: 70px;
    width: 150px; height: 150px;
    margin-left: -75px;
    border-radius: 50%;
    background: var(--ink-dark);
  }
  .front-brand {
    position: absolute;
    left: 0; right: 0; top: 252px;
    text-align: center;
  }
  .front-brand__name { font-size: 30px; letter-spacing: .5px; color: var(--ink-dark); }
  .front-brand__tag { font-size: 13px; color: var(--ink-soft); margin-top: 4px; letter-spacing: .3px; }
</style>
</head>
<body>

<section class="card card--back" aria-label="Business card back">
  <div class="back-brand">
    <div class="back-brand__name">R&amp;K PRENTISS</div>
    <div class="back-brand__tag">security services PTY. LTD</div>
  </div>
  <div class="back-divider"></div>
  <ul class="contact-list">
    <li class="contact-list__item">
      <svg class="contact-list__icon" viewBox="0 0 16 16"><circle cx="8" cy="8" r="8" fill="#f1f1f1"/><path d="M5 4.5l1.6-.4 1 2-1 .8a5 5 0 0 0 2.5 2.5l.8-1 2 1-.4 1.6c-3.5.2-6.7-3-6.5-6.5z" fill="#2f2f31"/></svg>
      0412555018
    </li>
    <li class="contact-list__item">
      <svg class="contact-list__icon" viewBox="0 0 16 16"><circle cx="8" cy="8" r="8" fill="#f1f1f1"/><path d="M5 4.5l1.6-.4 1 2-1 .8a5 5 0 0 0 2.5 2.5l.8-1 2 1-.4 1.6c-3.5.2-6.7-3-6.5-6.5z" fill="#2f2f31"/></svg>
      (03) 95550147
    </li>
    <li class="contact-list__item">
      <svg class="contact-list__icon" viewBox="0 0 16 16"><circle cx="8" cy="8" r="8" fill="#f1f1f1"/><rect x="4" y="5" width="8" height="6" fill="#2f2f31"/><path d="M4 5l4 3.2L12 5" stroke="#f1f1f1" stroke-width=".9" fill="none"/></svg>
      dale@prentiss.net.au
    </li>
    <li class="contact-list__item">
      <svg class="contact-list__icon" viewBox="0 0 16 16"><circle cx="8" cy="8" r="8" fill="#f1f1f1"/><rect x="4" y="5" width="8" height="6" fill="#2f2f31"/><path d="M4 5l4 3.2L12 5" stroke="#f1f1f1" stroke-width=".9" fill="none"/></svg>
      R.K@prentiss.net.au
    </li>
    <li class="contact-list__item">
      <svg class="contact-list__icon" viewBox="0 0 16 16"><circle cx="8" cy="8" r="8" fill="#f1f1f1"/><path d="M8 3.5a3 3 0 0 1 3 3c0 2.2-3 5.8-3 5.8S5 8.7 5 6.5a3 3 0 0 1 3-3z" fill="#2f2f31"/><circle cx="8" cy="6.5" r="1" fill="#f1f1f1"/></svg>
      P.O Box 48 Hillcrest Victoria 3184
    </li>
  </ul>
</section>

<section class="card card--front" aria-label="Business card front">
  <div class="front-mark"></div>
  <div class="front-brand">
    <div class="front-brand__name">R&amp;K PRENTISS</div>
    <div class="front-brand__tag">security services PTY. LTD</div>
  </div>
</section>

</body>
</html>
```